Health Care Company with Logo Needs Business Cards designed

We are a luxury behavioral health company looking for business cards design we already have a logo and are looking for someone to design a sophisticated luxurious looking business card. Please note that Card design should be captivating just like the logo and also encompass the logo color

Industry/Entity Type

Healthcare

Contact Information for Business Card

Logo,company name, tagline, my name and title, contact details, and physical address

```html
<!DOCTYPE html>
<html lang="en">
<head>
<meta charset="utf-8">
<title>Corva Behavioral Health – Business Card</title>
<link rel="stylesheet" href="https://fonts.googleapis.com/css2?family=Montserrat:wght@400;500;600;700&display=swap">
<style>
  :root {
    --page: #d9dccb;
    --card-dark: #0a0b0d;
    --card-white: #ffffff;
    --card-cream: #fbf7e1;
    --ink: #111111;
    --text-light: #e8e8e8;
    --accent-blue: #27a9e1;
    --brand-purple: #7b3a96;
    --shadow: rgba(0, 0, 0, 0.35);
  }
  * { margin: 0; padding: 0; box-sizing: border-box; }
  html, body {
    width: 1200px; height: 1000px; overflow: hidden;
    background: var(--page);
    font-family: "Montserrat", sans-serif;
  }
  .canvas { position: relative; width: 1200px; height: 1000px; }

  .card {
    position: absolute; left: 326px; width: 580px; height: 331px;
    background: var(--card-dark);
    border-radius: 3px;
    box-shadow: 0 8px 22px var(--shadow);
    overflow: hidden;
  }
  .card--front { top: 156px; }
  .card--back { top: 536px; }

  /* Front: name strip */
  .name-strip {
    position: absolute; left: 0; top: 0; width: 179px; height: 100%;
    background: var(--card-white);
    display: flex; align-items: center; justify-content: center; gap: 6px;
  }
  .name-strip .vertical {
    writing-mode: vertical-rl; transform: rotate(180deg);
  }
  .person-name {
    font-size: 33px; font-weight: 600; color: var(--ink); letter-spacing: 0.2px;
  }
  .person-title {
    font-size: 14px; font-weight: 500; color: var(--accent-blue); letter-spacing: 2.4px;
    text-align: right;
  }

  /* Front: contact list */
  .contact-list {
    position: absolute; left: 233px; top: 88px; list-style: none;
  }
  .contact-item {
    display: flex; align-items: flex-start; gap: 23px;
    color: var(--text-light); font-size: 21px; font-weight: 400; line-height: 28px;
    margin-bottom: 32px;
  }
  .contact-item:nth-child(3) { margin-top: -3px; }
  .contact-icon { width: 28px; height: 28px; flex: none; margin-top: 1px; }

  /* Back */
  .brand {
    position: absolute; left: 47px; top: 143px;
    display: flex; align-items: center; gap: 12px;
  }
  .brand-square { width: 40px; height: 40px; background: var(--brand-purple); flex: none; }
  .brand-name {
    font-size: 24px; font-weight: 600; color: var(--brand-purple); line-height: 1;
    letter-spacing: -0.2px;
  }
  .brand-tagline {
    font-size: 9.5px; font-weight: 700; color: var(--accent-blue);
    letter-spacing: 0.9px; text-transform: uppercase; margin-top: 5px;
  }
  .site-strip {
    position: absolute; right: 0; top: 0; width: 113px; height: 100%;
    background: var(--card-cream);
    display: flex; align-items: center; justify-content: center;
  }
  .site-url {
    writing-mode: vertical-rl; transform: rotate(180deg);
    font-size: 24px; font-weight: 500; color: var(--ink); letter-spacing: 0.3px;
  }
</style>
</head>
<body>
<main class="canvas">

  <section class="card card--front" aria-label="Business card front">
    <div class="name-strip">
      <div class="vertical">
        <div class="person-name">Daniel Reyes</div>
        <div class="person-title">PROPRIETOR</div>
      </div>
    </div>

    <ul class="contact-list">
      <li class="contact-item">
        <svg class="contact-icon" viewBox="0 0 28 28" aria-hidden="true">
          <rect width="28" height="28" rx="5" fill="var(--accent-blue)"/>
          <rect x="9" y="5" width="10" height="18" rx="2" fill="var(--card-dark)"/>
          <rect x="10.5" y="7" width="7" height="11" fill="var(--accent-blue)"/>
        </svg>
        <span>+ 000 12345 6789</span>
      </li>
      <li class="contact-item">
        <svg class="contact-icon" viewBox="0 0 28 28" aria-hidden="true">
          <rect width="28" height="28" rx="5" fill="var(--accent-blue)"/>
          <rect x="6" y="8" width="16" height="12" rx="1" fill="var(--card-dark)"/>
          <path d="M6.5 9 L14 15 L21.5 9" fill="none" stroke="var(--accent-blue)" stroke-width="1.8"/>
        </svg>
        <span>urname@mailbox.com</span>
      </li>
      <li class="contact-item">
        <svg class="contact-icon" viewBox="0 0 28 28" aria-hidden="true">
          <rect width="28" height="28" rx="5" fill="var(--accent-blue)"/>
          <path d="M14 5 C9.6 5 7.5 8 7.5 11.2 C7.5 15.5 14 23 14 23 C14 23 20.5 15.5 20.5 11.2 C20.5 8 18.4 5 14 5 Z" fill="var(--card-dark)"/>
          <circle cx="14" cy="11.3" r="2.6" fill="var(--accent-blue)"/>
        </svg>
        <span>Street Address Here<br>Singapore, 2222</span>
      </li>
    </ul>
  </section>

  <section class="card card--back" aria-label="Business card back">
    <div class="brand">
      <div class="brand-square" aria-hidden="true"></div>
      <div class="brand-text">
        <div class="brand-name">Corva Behavioral Health</div>
        <div class="brand-tagline">Dedicated to hope, healing and recovery</div>
      </div>
    </div>
    <div class="site-strip">
      <div class="site-url">www.sitename.com</div>
    </div>
  </section>

</main>
</body>
</html>
```